Geschäftspapiere für Softwareentwicklung/Consulting
Zielgruppe
Wir sind in der Softwareentwicklung / Consulting tätig und unterstützen durch externe Mitarbeit große und mittelständige Unternehmen.
Aufgabenstellung
Die Farben unseres Logos sollen aufgenommen werden. Der rechte Rand soll Angaben wie, Anschrift, Bankverbindung und Geschäftsdaten beinhalten - diese sollen nicht im Footer erscheinen. Das ganze sollte nicht zu bunt gestaltet werden.

```html
<!DOCTYPE html>
<html lang="de">
<head>
<meta charset="utf-8">
<title>fennrisoft – Briefbogen</title>
<link rel="stylesheet" href="https://fonts.googleapis.com/css2?family=Open+Sans:wght@400;600;700&display=swap">
<style>
  :root {
    --teal: #7cbcb3;
    --blue: #4a8fcb;
    --ink: #3a3a3a;
    --muted: #6a6a6a;
    --paper: #ffffff;
    --backdrop: #e6e6e6;
  }
  * { box-sizing: border-box; margin: 0; padding: 0; }
  html, body { width: 1200px; height: 1105px; overflow: hidden; }
  body {
    background: var(--backdrop);
    font-family: "Open Sans", sans-serif;
    color: var(--ink);
    position: relative;
  }
  .sheet {
    position: absolute;
    left: 224px; top: 20px;
    width: 752px; height: 1065px;
    background: var(--paper);
    box-shadow: 0 2px 8px rgba(0,0,0,.12);
    overflow: hidden;
  }
  .top-band {
    position: absolute; left: 0; top: 58px;
    width: 520px; height: 12px;
    background: var(--teal);
  }
  .brand {
    position: absolute; right: 46px; top: 100px;
    display: flex; align-items: center; gap: 10px;
  }
  .brand-dot { width: 34px; height: 34px; border-radius: 50%; background: var(--teal); }
  .brand-name { font-size: 34px; font-weight: 600; color: var(--ink); letter-spacing: -0.5px; }

  .address-window {
    position: absolute; left: 62px; top: 110px;
    width: 362px; height: 180px;
  }
  .address-window svg { position: absolute; inset: 0; }
  .return-line {
    position: absolute; left: 70px; top: 22px;
    font-size: 8.5px; color: var(--ink);
    border-bottom: 1px solid var(--ink);
    padding-bottom: 2px; white-space: nowrap;
  }
  .return-line .sender { font-weight: 600; font-size: 10px; }
  .return-line .sep { color: var(--teal); }
  .recipient {
    position: absolute; left: 30px; top: 60px;
    font-size: 12px; line-height: 15px; font-style: italic; color: var(--muted);
  }

  .sidebar {
    position: absolute; left: 540px; top: 170px; width: 190px;
    font-size: 9.5px; line-height: 14px; color: var(--muted);
  }
  .sidebar-block { padding-left: 12px; margin-bottom: 14px; }
  .sidebar-block.contact { border-left: 3px solid var(--blue); }
  .sidebar-block.business { border-left: 3px solid var(--teal); }
  .sidebar-heading { color: var(--teal); font-weight: 600; }
  .contact-row { display: flex; align-items: center; gap: 6px; }
  .contact-row svg { width: 10px; height: 10px; flex: none; }

  .marker {
    position: absolute; width: 0; height: 0;
    border-top: 4px solid transparent; border-bottom: 4px solid transparent;
    border-left: 6px solid var(--teal);
  }
  .letter {
    position: absolute; left: 70px; top: 370px; width: 620px;
    font-size: 14px; line-height: 19px; text-align: justify;
  }
  .greeting { margin-bottom: 14px; }
  .letter p + p { margin-top: 14px; }

  .signature {
    position: absolute; left: 480px; top: 830px;
    width: 200px; height: 80px;
    background: linear-gradient(120deg, rgba(60,60,60,0) 0%, rgba(60,60,60,.08) 50%, rgba(60,60,60,0) 100%);
    border-radius: 40px;
  }

  .footer-band-left {
    position: absolute; left: 0; top: 985px; width: 60px; height: 10px; background: var(--teal);
  }
  .footer-dot {
    position: absolute; left: 72px; top: 977px; width: 26px; height: 26px;
    border-radius: 50%; background: var(--teal);
  }
  .footer-band-right {
    position: absolute; left: 110px; top: 985px; right: 0; height: 10px; background: var(--teal);
  }
</style>
</head>
<body>
  <main class="sheet">
    <div class="top-band"></div>

    <div class="brand">
      <span class="brand-dot"></span>
      <span class="brand-name">fennrisoft</span>
    </div>

    <section class="address-window">
      <svg viewBox="0 0 362 180" fill="none" stroke="#555" stroke-width="1">
        <path d="M2 22 V10 Q2 2 10 2 H22"/>
        <path d="M340 2 H352 Q360 2 360 10 V22"/>
        <path d="M2 158 V170 Q2 178 10 178 H22"/>
        <path d="M340 178 H352 Q360 178 360 170 V158"/>
      </svg>
      <div class="return-line">
        <span class="sender">fennrisoft</span>
        <span class="sep">●</span> Weidenweg 8 <span class="sep">●</span> D-40000 Talstadt
      </div>
      <div class="recipient">
        Herr.:<br>Anton Kessler<br>Web Master<br>City
      </div>
    </section>

    <aside class="sidebar">
      <div class="sidebar-block contact">
        Am Lindenhof 12<br>
        64000 Talheim
        <div class="contact-row">
          <svg viewBox="0 0 10 10"><path d="M2 1 L4 1 L5 3 L4 4 Q5 6 6 6 L7 5 L9 6 L9 8 Q8 9 7 9 Q1 8 1 2 Q1 1 2 1Z" fill="#4a8fcb"/></svg>
          + 49 (0) 0000 4120 - 500
        </div>
        <div class="contact-row">
          <svg viewBox="0 0 10 10" fill="none" stroke="#4a8fcb" stroke-width="1"><circle cx="5" cy="5" r="4"/><path d="M1 5 H9 M5 1 Q2 5 5 9 M5 1 Q8 5 5 9"/></svg>
          www.fennrisoft.com
        </div>
        <div class="contact-row">
          <svg viewBox="0 0 10 10" fill="none" stroke="#4a8fcb" stroke-width="1"><rect x="1" y="2" width="8" height="6"/><path d="M1 2 L5 6 L9 2"/></svg>
          info@fennrisoft.com
        </div>
        Geschäftsführer
      </div>
      <div class="sidebar-block business">
        <div class="sidebar-heading">Konto</div>
        Kreissparkasse Talheim<br>
        (BLZ 00000000), Kto.-Nr. 1234567<br>
        IBAN DE00000000000001234567<br>
        SWIFT-BIC XXXXXXXX1TAL
        <div class="sidebar-heading">Identnummern</div>
        Steuernummer: 000 0000 12345<br>
        USt-IdNr.: 000012345
      </div>
    </aside>

    <span class="marker" style="left:22px; top:300px;"></span>
    <span class="marker" style="left:22px; top:560px;"></span>

    <article class="letter">
      <p class="greeting">Lorem ipsum dolor sit amet,</p>
      <p>Lorem ipsum dolor sit amet, consectetur adipiscing elit. Donec orci purus, luctus vitae dignissim eu, iaculis sed purus. Vivamus faucibus, ipsum nec aliquet viverra, leo mauris condimentum ligula, sit amet sagittis enim ligula quis arcu. Nam egestas tortor id nisi porttitor mattis. In tortor ante, ultricies in suscipit a, tempus non massa. Vivamus et auctor mi. Fusce vel massa nulla. Phasellus nec eros mauris, et scelerisque orci. Donec malesuada orci vitae nulla accumsan porta a id massa. Quisque accumsan iaculis magna sit amet fringilla. Maecenas consequat, magna eget tincidunt semper, odio nibh rutrum mi, id feugiat ante nisi eu risus. Vestibulum nunc orci, rhoncus a placerat in, ultricies in mi. Cras mattis varius eros, vel fringilla nisi suscipit eget.</p>
      <p>Quisque scelerisque sagittis nulla at porttitor. Mauris a justo et tellus interdum tristique. Sed id augue vitae urna euismod commodo aliquet a quam. Pellentesque arcu velit, cursus et malesuada ut, consequat et diam. Nullam erat sem, rhoncus id ullamcorper vitae, rhoncus et arcu. In ultricies ultricies nulla, ut rutrum nisi iaculis at. Donec eu magna a metus ornare faucibus. Fusce aliquet faucibus ultricies. Morbi semper, est id tincidunt gravida, sem arcu adipiscing lacus, ac bibendum nulla leo eu purus. Quisque nec diam sed risus consectetur a ccumsan quis quis nibh. Vestibulum id purus lorem.</p>
      <p>Vivamus vehicula accumsan lacinia. Aliquam erat volutpat. Pellentesque consequat venenatis velit non gravida. Etiam et sem et nulla congue aliquam sed eget augue. Nulla facilisi. Pellentesque habitant morbi tristique senectus et netus et malesuada fames ac turpis egestas. Nulla a elit at sem iaculis congue. Nullam mollis tristique lobortis.</p>
    </article>

    <div class="signature" role="img" aria-label="Handschriftliche Unterschrift"></div>

    <div class="footer-band-left"></div>
    <span class="footer-dot"></span>
    <div class="footer-band-right"></div>
  </main>
</body>
</html>
```